Verpackungsdesign für Kaffeefilter
Sehr gute Kommunikation! Schnelle und zuverlässige Bearbeitung! Klasse, gerne wieder.
Zielgruppe
Wir, TAVERO GmbH, sind größter Hersteller von privat label Kaffeefiltern. Für unsere Eigenmarke LINDA Premium Kaffeefilter Größe 4, 80 Stück, braun wird ein kreatives und frisches Verpackungsdesign benötigt. Zielgruppe für die LINDA Premium Kaffeefilter sind internationale Filterkaffeetrinker im Altersspektrum 18 bis 50 Jahre.
Aufgabenstellung
Wir wünschen uns ein Faltschachtel - Design, welches frisch und jugendlich, luxuriös / hochwertig aber nicht opulent/barock, smart und reduziert (nicht überladen), nicht verspielt, abstrakt und schematisch sowie skandinavisch und modern, für einen internationalen Kundenkreis, ist. Die gesamte Faltschachtel (beiliegende Stanze) soll gestaltet werden.
Es sollen weder eine fotografische Filterabbildung noch andere Fotos auf der Verpackung sein.
WGR Logo und Grüner Falke sowie Herstelleradresse und 3 Barcodefelder werden benötigt.
ACHTUNG: Die Aufreißlasche ist die Rückseite! Die Front steht im Tray. Es wird ca. 25% im unteren Teil der Faltschachtel vom Tray verdeckt.

```html
<!DOCTYPE html>
<html lang="de">
<head>
<meta charset="utf-8">
<title>TAVERO Kaffeefilter – Faltschachtel</title>
<link rel="stylesheet" href="https://fonts.googleapis.com/css2?family=Montserrat:wght@500;600;700&display=swap">
<style>
  :root {
    --paper: #ffffff;
    --board: #e8dfcc;
    --ink: #3a3430;
    --orange: #d9482a;
    --yellow: #d6a42a;
    --cut: #e2358e;
    --badge: #f4efe4;
  }
  html, body { margin: 0; padding: 0; width: 888px; height: 1200px; overflow: hidden; background: var(--paper); }
  .dieline { display: block; width: 888px; height: 1200px; font-family: "Montserrat", sans-serif; }
  .panel { fill: var(--board); }
  .cutline { fill: none; stroke: var(--cut); stroke-width: 0.8; }
  .title { font-weight: 700; fill: var(--ink); letter-spacing: -0.5px; }
  .brand { font-weight: 700; fill: var(--ink); letter-spacing: 1px; }
  .variant-box { fill: var(--ink); }
  .variant { font-weight: 600; fill: var(--board); letter-spacing: 1px; }
  .meta { font-weight: 600; fill: var(--ink); }
  .glue { font-weight: 500; fill: var(--cut); font-size: 10px; }
  .badge { fill: var(--badge); stroke: var(--ink); stroke-width: 0.6; }
  .title-plate { fill: var(--board); }
</style>
</head>
<body>
<svg class="dieline" viewBox="0 0 1000 1350" preserveAspectRatio="none" xmlns="http://www.w3.org/2000/svg">
  <defs>
    <radialGradient id="brush-lid" cx="50%" cy="55%" r="60%">
      <stop offset="0" stop-color="#d9482a" stop-opacity="0.85"/>
      <stop offset="0.45" stop-color="#d6a42a" stop-opacity="0.7"/>
      <stop offset="0.8" stop-color="#3a3430" stop-opacity="0.35"/>
      <stop offset="1" stop-color="#e8dfcc" stop-opacity="0"/>
    </radialGradient>
    <radialGradient id="brush-front" cx="55%" cy="40%" r="65%">
      <stop offset="0" stop-color="#d6a42a" stop-opacity="0.8"/>
      <stop offset="0.4" stop-color="#d9482a" stop-opacity="0.65"/>
      <stop offset="0.8" stop-color="#3a3430" stop-opacity="0.35"/>
      <stop offset="1" stop-color="#e8dfcc" stop-opacity="0"/>
    </radialGradient>
  </defs>

  <!-- Lid and side flaps -->
  <rect class="panel" x="222" y="108" width="556" height="375"/>
  <rect class="panel" x="115" y="115" width="107" height="368"/>
  <rect class="panel" x="778" y="115" width="107" height="368"/>
  <rect role="img" aria-label="Abstrakte Pinselstriche in Orange, Gelb und Dunkelbraun" x="222" y="108" width="556" height="375" fill="url(#brush-lid)"/>

  <!-- Middle band -->
  <rect class="panel" x="130" y="483" width="740" height="122"/>

  <!-- Front and side flaps -->
  <rect class="panel" x="222" y="605" width="556" height="367"/>
  <rect class="panel" x="115" y="605" width="107" height="363"/>
  <rect class="panel" x="778" y="605" width="107" height="363"/>
  <rect role="img" aria-label="Abstrakte Pinselstriche in Orange, Gelb und Dunkelbraun" x="222" y="605" width="556" height="367" fill="url(#brush-front)"/>

  <!-- Bottom band and glue flap -->
  <rect class="panel" x="130" y="972" width="740" height="123"/>
  <rect class="panel" x="220" y="1095" width="560" height="135"/>

  <!-- Cut and crease lines -->
  <g class="cutline">
    <rect x="222" y="108" width="556" height="375"/>
    <rect x="115" y="115" width="107" height="368"/>
    <rect x="778" y="115" width="107" height="368"/>
    <rect x="125" y="125" width="87" height="348"/>
    <rect x="788" y="125" width="87" height="348"/>
    <path d="M245 310 L245 500 Q245 525 270 525 L730 525 Q755 525 755 500 L755 310 L595 130 L405 130 Z"/>
    <rect x="130" y="483" width="740" height="122"/>
    <rect x="140" y="493" width="72" height="102"/>
    <rect x="788" y="493" width="72" height="102"/>
    <rect x="222" y="605" width="556" height="367"/>
    <rect x="115" y="605" width="107" height="363"/>
    <rect x="778" y="605" width="107" height="363"/>
    <rect x="130" y="625" width="58" height="327"/>
    <rect x="812" y="625" width="58" height="327"/>
    <rect x="130" y="972" width="740" height="123"/>
    <rect x="140" y="982" width="72" height="103"/>
    <rect x="788" y="982" width="72" height="103"/>
    <path d="M220 1095 L220 1230 L780 1230 L780 1095"/>
    <path d="M230 1105 L230 1220 L310 1220 L390 1130 L610 1130 L690 1220 L770 1220 L770 1105"/>
    <rect x="235" y="1118" width="136" height="20"/>
    <rect x="628" y="1118" width="136" height="20"/>
    <rect x="235" y="1182" width="76" height="20"/>
    <rect x="688" y="1182" width="76" height="20"/>
  </g>

  <!-- Lid content (upside down) -->
  <g class="lid" transform="rotate(180 500 340)">
    <rect class="title-plate" x="320" y="313" width="360" height="55"/>
    <text class="title" x="500" y="358" font-size="44" text-anchor="middle">KAFFEEFILTER</text>
    <rect class="variant-box" x="457" y="374" width="86" height="30"/>
    <text class="variant" x="500" y="396" font-size="16" text-anchor="middle">BRAUN</text>
    <rect class="variant-box" x="424" y="280" width="14" height="14"/>
    <text class="brand" x="505" y="294" font-size="22" text-anchor="middle">TAVERO</text>
  </g>

  <!-- Certificate placeholders (plain shapes) -->
  <rect class="badge" x="237" y="130" width="78" height="28" rx="3"/>
  <circle class="badge" cx="276" cy="205" r="38"/>
  <rect class="badge" x="643" y="131" width="119" height="50" rx="4"/>

  <!-- Left lid flap (rotated) -->
  <g transform="translate(172 142) rotate(90)">
    <text class="title" x="0" y="0" font-size="24">KAFFEEFILTER</text>
  </g>
  <g transform="translate(192 188) rotate(90)">
    <rect class="variant-box" x="0" y="-16" width="10" height="10"/>
    <text class="brand" x="14" y="-6" font-size="14">TAVERO</text>
  </g>
  <g transform="translate(141 203) rotate(90)">
    <rect class="variant-box" x="0" y="-14" width="44" height="16"/>
    <text class="variant" x="22" y="-3" font-size="8" text-anchor="middle">BRAUN</text>
  </g>

  <!-- Right lid flap (rotated) -->
  <g transform="translate(834 458) rotate(-90)">
    <text class="title" x="0" y="0" font-size="24">KAFFEEFILTER</text>
  </g>
  <g transform="translate(806 412) rotate(-90)">
    <rect class="variant-box" x="0" y="-10" width="10" height="10"/>
    <text class="brand" x="14" y="0" font-size="14">TAVERO</text>
  </g>
  <g transform="translate(858 395) rotate(-90)">
    <rect class="variant-box" x="0" y="-14" width="44" height="16"/>
    <text class="variant" x="22" y="-3" font-size="8" text-anchor="middle">BRAUN</text>
  </g>

  <!-- Front content -->
  <g class="front">
    <text class="meta" x="245" y="640" font-size="16">Größe 4</text>
    <text class="meta" x="755" y="640" font-size="16" text-anchor="end">80 Stück</text>
    <rect class="variant-box" x="427" y="685" width="18" height="18"/>
    <text class="brand" x="510" y="704" font-size="28" text-anchor="middle">TAVERO</text>
    <rect class="title-plate" x="322" y="718" width="356" height="52"/>
    <text class="title" x="500" y="762" font-size="44" text-anchor="middle">KAFFEEFILTER</text>
    <rect class="variant-box" x="457" y="779" width="86" height="30"/>
    <text class="variant" x="500" y="801" font-size="16" text-anchor="middle">BRAUN</text>
  </g>

  <!-- Bottom band content -->
  <g class="bottom">
    <rect class="variant-box" x="358" y="993" width="13" height="13"/>
    <text class="brand" x="415" y="1007" font-size="18" text-anchor="middle">TAVERO</text>
    <text class="title" x="405" y="1042" font-size="29" text-anchor="middle">KAFFEEFILTER</text>
    <rect class="variant-box" x="378" y="1054" width="55" height="19"/>
    <text class="variant" x="405.5" y="1068" font-size="11" text-anchor="middle">BRAUN</text>
  </g>

  <!-- Glue markers -->
  <text class="glue" x="285" y="1132" text-anchor="middle">KLEJ</text>
  <text class="glue" x="716" y="1132" text-anchor="middle">KLEJ</text>
  <text class="glue" x="254" y="1197" text-anchor="middle">KLEJ</text>
  <text class="glue" x="746" y="1197" text-anchor="middle">KLEJ</text>
</svg>
</body>
</html>
```